advertising board Hovarlunde BV

I have an advertisement spot in a small indoor football stadium, with the size of 1.00 x 22.00 meters. I want to show a design that stands out. My company works in Civil constructions and actually installs steel sheet piles and earth retaining walls in the most difficult to reach locations.

```html
<!DOCTYPE html>
<html lang="nl">
<head>
<meta charset="utf-8">
<title>Hovarlunde BV – boarding</title>
<link href="https://fonts.googleapis.com/css2?family=Open+Sans:wght@600;700&display=swap" rel="stylesheet">
<style>
  :root {
    --page: #c8c9c8;
    --board: #ffffff;
    --band: #231f20;
    --brand-blue: #1b8fd6;
    --accent-blue: #2a78c4;
    --machine: #1e1e1e;
    --tag-text: #ffffff;
  }
  * { margin: 0; padding: 0; box-sizing: border-box; }
  html, body {
    width: 1200px; height: 1099px; overflow: hidden;
    background: var(--page);
    font-family: "Open Sans", Arial, sans-serif;
  }
  .canvas {
    width: 1200px; height: 1099px;
    display: flex; align-items: center; justify-content: center;
  }
  .boarding {
    width: 1158px; height: 52px;
    background: var(--board);
    position: relative;
    display: flex; flex-direction: column;
  }
  .boarding__top {
    height: 38px;
    display: flex; align-items: flex-end;
    padding: 0 6px;
  }
  .machine {
    flex: none;
    height: 32px;
    background: linear-gradient(180deg, #3a3a3a, var(--machine));
    border-radius: 3px;
    opacity: .9;
  }
  .machine--wide { width: 64px; }
  .machine--mid { width: 54px; }
  .machine--loader { width: 58px; }
  .brand {
    flex: 1;
    text-align: center;
    font-weight: 700;
    font-size: 30px;
    line-height: 36px;
    color: var(--brand-blue);
    white-space: nowrap;
    letter-spacing: .5px;
  }
  .boarding__band {
    height: 14px;
    background: var(--band);
    display: flex; align-items: center;
    padding-left: 4px;
    overflow: hidden;
  }
  .tagline {
    flex: 1;
    color: var(--tag-text);
    font-weight: 700;
    font-size: 9.6px;
    white-space: nowrap;
    text-align: center;
    letter-spacing: .1px;
  }
  .divider {
    flex: none;
    width: 4px; height: 14px;
    background: var(--accent-blue);
    transform: skewX(-18deg);
    margin: 0 4px;
  }
</style>
</head>
<body>
  <main class="canvas">
    <section class="boarding" aria-label="Reclamebord Hovarlunde BV">
      <div class="boarding__top">
        <div class="machine machine--wide" role="img" aria-label="Silhouet van een graafmachine met heiblok"></div>
        <span class="brand">Hovarlunde BV</span>
        <div class="machine machine--mid" role="img" aria-label="Silhouet van een rupsgraafmachine"></div>
        <span class="brand">Hovarlunde BV</span>
        <div class="machine machine--wide" role="img" aria-label="Silhouet van een damwandmachine met lange giek"></div>
        <span class="brand">Hovarlunde BV</span>
        <div class="machine machine--loader" role="img" aria-label="Silhouet van een wiellader"></div>
      </div>
      <div class="boarding__band">
        <span class="tagline">damwandconstructies - onderhoud - beschoeiingen - grondwerk</span>
        <span class="divider"></span>
        <span class="tagline">damwandconstructies - onderhoud - beschoeiingen - grondwerk</span>
        <span class="divider"></span>
        <span class="tagline">damwandconstructies - onderhoud - beschoeiingen - grondwerk</span>
      </div>
    </section>
  </main>
</body>
</html>
```